Brand Business Card for Hotel Cloud Management System

Hello designers,
we are looking for a new brand business card for our product Roomvanta. Our brand Roomvanta is a hotel management system for small hotels, B&B, guesthouses etc. and just recently we are expanding our offer to other European markets. Therefore we need a business card that will communicate not only to the end-users (hoteliers) but also to potential business partners/ We would like the brand business card to be professional looking, but not too serius, modern, elegant, clean, Our brand color is orange, dark grey and it would be nice to see both combined.

Please visit our website www.roomvanta-example.eu to get more impression on what our brand roomvanta stands for.

Please find attached roomvanta logo.

Target Market(s)

small hotels, hoteliers, B&B owners, potential business partners

Industry/Entity Type

Software Service

Contact Information for Business Card

Roomvanta
- hotel software solutions - web booking engine - multi channel manager
www.roomvanta-example.eu
T: +38614007300
E: info@roomvanta-example.net

Font styles to use
Serif
Sans Serif

Colors
f37122
aaaaaa
606060
f6f6f6

Requirements
Must have
• Logo of the brand
• the layout of the business card should be in connection with the look and feel of the website roomvanta-example.eu and logo roomvanta;

```html
<!DOCTYPE html>
<html lang="en">
<head>
<meta charset="utf-8">
<title>Roomvanta Business Card</title>
<link rel="stylesheet" href="https://fonts.googleapis.com/css2?family=Arimo:wght@400;700&display=swap">
<style>
  :root {
    --stage: #2a2a2a;
    --paper-top: #ffffff;
    --paper-bottom: #e6e6e6;
    --brand-orange: #f37122;
    --band-orange: #e5801f;
    --charcoal: #262626;
    --ink: #1f1f1f;
    --soft-white: #f6f6f6;
    --muted: #aaaaaa;
  }
  html, body {
    margin: 0;
    width: 1200px;
    height: 997px;
    overflow: hidden;
    background: var(--stage);
    font-family: "Arimo", Arial, sans-serif;
  }
  .business-card {
    position: absolute;
    left: 190px;
    top: 264px;
    width: 820px;
    height: 470px;
    border-radius: 20px;
    overflow: hidden;
    background: var(--charcoal);
  }
  .card-head {
    height: 250px;
    background: linear-gradient(180deg, var(--paper-top) 0%, var(--paper-bottom) 100%);
    display: flex;
    align-items: center;
    justify-content: center;
  }
  .brand-name {
    margin: 18px 0 0;
    font-size: 86px;
    font-weight: 700;
    letter-spacing: -2px;
    color: var(--ink);
  }
  .name-band {
    height: 68px;
    background: var(--band-orange);
    border-bottom: 2px solid #f2b27a;
    padding-left: 250px;
    display: flex;
    flex-direction: column;
    justify-content: center;
  }
  .person-name {
    margin: 0;
    font-size: 24px;
    font-weight: 700;
    letter-spacing: 0.5px;
    color: var(--ink);
  }
  .person-role {
    margin: 2px 0 0 26px;
    font-size: 16px;
    color: var(--soft-white);
  }
  .card-foot {
    position: relative;
    height: 150px;
  }
  .services {
    position: absolute;
    right: 28px;
    top: -40px;
    margin: 0;
    padding: 0;
    list-style: none;
    text-align: right;
  }
  .services li {
    font-size: 15px;
    letter-spacing: 0.4px;
    color: var(--soft-white);
    line-height: 31px;
  }
  .services li::after {
    content: "";
    display: inline-block;
    width: 5px;
    height: 5px;
    margin-left: 12px;
    border-radius: 50%;
    background: var(--soft-white);
    vertical-align: middle;
  }
  .contacts {
    position: absolute;
    left: 30px;
    bottom: 22px;
    margin: 0;
    padding: 0;
    list-style: none;
  }
  .contacts li {
    display: flex;
    align-items: center;
    gap: 16px;
    font-size: 18px;
    line-height: 34px;
    color: var(--soft-white);
  }
  .contacts .web-link {
    font-weight: 700;
    color: var(--brand-orange);
  }
  .contact-icon {
    width: 20px;
    height: 20px;
    flex: none;
  }
</style>
</head>
<body>
  <article class="business-card">
    <header class="card-head">
      <h1 class="brand-name">Roomvanta</h1>
    </header>

    <section class="name-band">
      <p class="person-name">LENA MAROVIC</p>
      <p class="person-role">Managing Director</p>
    </section>

    <section class="card-foot">
      <ul class="services">
        <li>HOTEL SOFTWARE SOLUTIONS</li>
        <li>WEB BOOKING ENGINE</li>
        <li>MULTI CHANNEL MANAGER</li>
      </ul>

      <ul class="contacts">
        <li>
          <svg class="contact-icon" viewBox="0 0 20 20" aria-hidden="true">
            <circle cx="10" cy="10" r="10" fill="#f0c49a"/>
            <path d="M6.5 5.5c.6-.5 1.4-.4 1.8.2l.8 1.3c.3.5.2 1.1-.2 1.4l-.6.5c.6 1.3 1.5 2.2 2.8 2.8l.5-.6c.3-.4.9-.5 1.4-.2l1.3.8c.6.4.7 1.2.2 1.8-.9 1-2.3 1.2-3.6.5-2-1.1-3.6-2.7-4.7-4.7-.7-1.3-.5-2.7.3-3.8z" fill="#262626"/>
          </svg>
          <span>+38614007300</span>
        </li>
        <li>
          <svg class="contact-icon" viewBox="0 0 20 20" aria-hidden="true">
            <circle cx="10" cy="10" r="10" fill="#f0c49a"/>
            <rect x="5" y="6.5" width="10" height="7" rx="1" fill="#262626"/>
            <path d="M5.5 7l4.5 3.6L14.5 7" stroke="#f0c49a" stroke-width="1" fill="none"/>
          </svg>
          <span>info@roomvanta-example.net</span>
        </li>
        <li>
          <svg class="contact-icon" viewBox="0 0 20 20" aria-hidden="true">
            <circle cx="10" cy="10" r="10" fill="#f0c49a"/>
            <circle cx="10" cy="10" r="5" fill="none" stroke="#262626" stroke-width="1.3"/>
            <path d="M5 10h10M10 5c-2.2 2.8-2.2 7.2 0 10M10 5c2.2 2.8 2.2 7.2 0 10" stroke="#262626" stroke-width="1" fill="none"/>
          </svg>
          <span class="web-link">www.roomvanta-example.eu</span>
        </li>
      </ul>
    </section>
  </article>
</body>
</html>
```